Pathways to Brightmoor Land Ventures

size of the ad - 8”x 10.75" plus 0.25" bleed
I would like an ad for a magazine that will stand out and make people want to read the ad.
The ad should not be crowded and people reading the ad will be able to read the text.
I would like it to be a creative and modern-day design.
the list of topics should not be the focus of the ad.
the text is attached.
If you decide to use people in the ad then please no ladies.
please note that leave over 1 inch for the bottom of the footer

```html
<!DOCTYPE html>
<html lang="en">
<head>
<meta charset="utf-8">
<title>Real Estate Course – Pathways to Brightmoor Land Ventures</title>
<link href="https://fonts.googleapis.com/css2?family=Teko:wght@500;600&family=Barlow:wght@400&family=Roboto+Condensed:ital,wght@0,400;0,700;1,700&family=Archivo:ital,wght@1,900&family=Open+Sans:wght@400;600&display=swap" rel="stylesheet">
<style>
  :root {
    --sky-light: #d9f8ff;
    --sky-mid: #5fdcfc;
    --sky-deep: #0ccbf8;
    --navy: #0b3a9c;
    --ink: #2f3034;
    --sun: #fbf70a;
    --panel: #88e8fd;
  }
  * { margin: 0; padding: 0; box-sizing: border-box; }
  html, body { width: 997px; height: 1200px; overflow: hidden; background: #ffffff; }
  .ad {
    position: relative;
    width: 997px;
    height: 1200px;
    overflow: hidden;
    background:
      radial-gradient(ellipse 560px 420px at 740px 120px, var(--sky-light) 0%, var(--sky-mid) 55%, transparent 100%),
      linear-gradient(180deg, var(--sky-mid) 0%, var(--sky-deep) 100%);
  }
  .course-title {
    position: absolute;
    left: 104px;
    top: 72px;
    font-family: "Teko", sans-serif;
    font-weight: 600;
    color: var(--navy);
    line-height: 0.82;
    text-transform: uppercase;
  }
  .course-title span { display: block; }
  .course-title .line-real { font-size: 160px; letter-spacing: 1px; }
  .course-title .line-estate { font-size: 112px; margin-top: 8px; }
  .course-title .line-course { font-size: 100px; margin-top: 8px; }
  .program-name {
    position: absolute;
    left: 106px;
    top: 398px;
    font-family: "Barlow", sans-serif;
    font-weight: 400;
    color: var(--ink);
    text-transform: uppercase;
    line-height: 1.05;
  }
  .program-name span { display: block; }
  .program-name .small { font-size: 38px; letter-spacing: 1px; }
  .program-name .large { font-size: 46px; letter-spacing: 1.5px; }
  .hero-photo {
    position: absolute;
    left: 508px;
    top: 84px;
    width: 489px;
    height: 456px;
  }
  .slogan-band {
    position: absolute;
    left: 0;
    top: 579px;
    width: 944px;
    height: 52px;
    background: var(--sun);
    border-radius: 0 26px 26px 0;
    box-shadow: 0 18px 24px -14px rgba(0, 70, 110, 0.35);
    display: flex;
    align-items: center;
    padding-left: 107px;
    font-family: "Roboto Condensed", sans-serif;
    font-weight: 700;
    font-size: 29px;
    color: var(--ink);
    text-transform: uppercase;
    white-space: nowrap;
  }
  .location {
    position: absolute;
    left: 0;
    width: 997px;
    top: 712px;
    text-align: center;
    padding-left: 6px;
    font-family: "Archivo", sans-serif;
    font-weight: 900;
    font-style: italic;
    font-size: 50px;
    color: var(--navy);
    letter-spacing: 1px;
  }
  .highlights {
    position: absolute;
    top: 777px;
    left: 111px;
    display: flex;
    gap: 10px;
  }
  .highlight {
    height: 58px;
    background: var(--sun);
    border-radius: 12px;
    display: flex;
    align-items: center;
    justify-content: center;
    text-align: center;
    font-family: "Roboto Condensed", sans-serif;
    font-weight: 400;
    font-size: 18px;
    line-height: 1.12;
    color: var(--navy);
  }
  .highlight.wide { width: 216px; }
  .highlight.narrow { width: 151px; }
  .audience {
    position: absolute;
    left: 0;
    width: 997px;
    top: 848px;
    padding-left: 50px;
    text-align: center;
    font-family: "Roboto Condensed", sans-serif;
    font-weight: 700;
    font-style: italic;
    font-size: 18px;
    color: var(--navy);
    text-transform: uppercase;
  }
  .topics {
    position: absolute;
    left: 107px;
    top: 946px;
    border-left: 5px solid var(--sun);
    padding-left: 11px;
    font-family: "Open Sans", sans-serif;
    color: var(--navy);
    font-size: 16px;
    line-height: 25px;
  }
  .topics h2 {
    font-size: 16px;
    font-weight: 600;
    text-transform: uppercase;
  }
  .topics p { white-space: nowrap; }
  .footer-panel {
    position: absolute;
    left: 30px;
    top: 1089px;
    width: 941px;
    height: 92px;
    background: var(--panel);
    border-radius: 14px;
  }
</style>
</head>
<body>
  <main class="ad">
    <h1 class="course-title">
      <span class="line-real">Real</span>
      <span class="line-estate">Estate</span>
      <span class="line-course">Course</span>
    </h1>

    <svg class="hero-photo" role="img" aria-label="Photo of an open hand holding a model two-storey house with a porch" viewBox="0 0 489 456">
      <defs>
        <radialGradient id="heroGlow" cx="0.45" cy="0.4" r="0.6">
          <stop offset="0" stop-color="#c9a97a" stop-opacity="0.55"/>
          <stop offset="0.6" stop-color="#d7b48f" stop-opacity="0.25"/>
          <stop offset="1" stop-color="#d7b48f" stop-opacity="0"/>
        </radialGradient>
      </defs>
      <rect width="489" height="456" fill="url(#heroGlow)"/>
    </svg>

    <h2 class="program-name">
      <span class="small">Pathways to</span>
      <span class="large">Brightmoor Land</span>
      <span class="large">Ventures</span>
    </h2>

    <div class="slogan-band">Investing in knowledge is investing in opportunities</div>

    <div class="location">HALDEN</div>

    <ul class="highlights">
      <li class="highlight wide">10-Tuesday<br>evenings sessions</li>
      <li class="highlight narrow">Starting<br>Feb.28</li>
      <li class="highlight wide">Limited Partial<br>Scholarships</li>
      <li class="highlight wide">Early Bird<br>Special</li>
    </ul>

    <p class="audience">For those that started or would like to go into real estate</p>

    <section class="topics">
      <h2>Topics : Partial Listing</h2>
      <p>Real estate investment strategies&nbsp; | Due diligence | Financing | Underwriting</p>
      <p>Property management | Real estate Legal basics | Sourcing deals | Syndication</p>
      <p>Dealing with brokers | Tax fundamentals</p>
    </section>

    <div class="footer-panel"></div>
  </main>
</body>
</html>
```